Letterhead Design

We need a new Letterhead design for a 30 year old Electrical Company. We service domestic and commercial places. We have a logo recently made so to incorporate that. Using same colours or interested to see others added.
Would like to see a couple of options with all the info in letterhead, then another with info in a footnote down the bottom.

info needed to be added:

-Lic. No 48162
8/22-24 Larkin Rd, Tolvern 2087
W - brightcoilpower.com.au
T - (02) 9471 3825
M - 0427 593 168
E - info@brightcoilpower.com.au
ABN: 42 597 214 630

Electrical

```html
<!DOCTYPE html>
<html lang="en">
<head>
<meta charset="utf-8">
<title>Brightcoil Power Letterhead</title>
<link rel="stylesheet" href="https://fonts.googleapis.com/css2?family=Open+Sans:wght@400;600;700&family=Montserrat:wght@400&display=swap">
<style>
  :root {
    --backdrop: #e6e6e6;
    --paper: #ffffff;
    --ink: #222222;
    --brand-dark: #1f2b33;
    --accent: #e8962a;
  }
  * { box-sizing: border-box; margin: 0; padding: 0; }
  html, body { width: 1200px; height: 985px; overflow: hidden; }
  body {
    background: var(--backdrop);
    font-family: "Open Sans", Arial, sans-serif;
    color: var(--ink);
    position: relative;
  }
  .letterhead {
    position: absolute;
    left: 282px; top: 42px;
    width: 636px; height: 900px;
    background: var(--paper);
    box-shadow: 0 2px 10px rgba(0,0,0,0.12);
  }
  .contact-block {
    position: absolute;
    left: 400px; top: 64px;
    font-size: 10.5px; line-height: 16px;
  }
  .contact-block .label { color: var(--accent); font-weight: 700; }
  .brand {
    position: absolute;
    left: 64px; top: 140px;
    display: flex; align-items: center; gap: 10px;
  }
  .brand-mark { width: 16px; height: 16px; background: var(--accent); }
  .brand-name {
    font-size: 24px; font-weight: 600;
    color: var(--brand-dark); letter-spacing: 0.2px;
  }
  .letter {
    position: absolute;
    left: 64px; top: 240px;
    width: 508px;
    font-size: 10.5px; line-height: 15px;
  }
  .letter-date, .letter-greeting { font-weight: 700; font-size: 12.5px; line-height: 18px; }
  .letter-greeting { margin-bottom: 16px; }
  .letter p.body-text { margin-bottom: 16px; text-align: justify; }
  .signature { margin-top: 26px; }
  .signature-name {
    font-family: "Montserrat", Arial, sans-serif;
    font-size: 20px; color: var(--brand-dark);
  }
  .signature-role { font-size: 9.5px; }
  .footer-note {
    position: absolute;
    left: 64px; bottom: 56px;
    border-left: 2px solid var(--accent);
    padding-left: 12px;
    font-size: 10.5px; line-height: 36px;
  }
  .footer-note .label { color: var(--accent); font-weight: 700; }
</style>
</head>
<body>
  <main class="letterhead">
    <address class="contact-block" style="font-style:normal">
      <div><span class="label">T</span> - (02) 9471 3825</div>
      <div><span class="label">M</span> - 0427 593 168</div>
      <div><span class="label">W</span> - www.brightcoilpower.com.au</div>
      <div><span class="label">E</span> - info@brightcoilpower.com.au</div>
      <div><span class="label">A</span> - 8/22-24 Larkin Rd, Tolvern 2087</div>
    </address>

    <div class="brand">
      <span class="brand-mark"></span>
      <span class="brand-name">Brightcoil Power</span>
    </div>

    <article class="letter">
      <div class="letter-date">Aug/08/2016</div>
      <div class="letter-greeting">Dear Peter,</div>
      <p class="body-text">Thank you for choosing our team for your recent electrical works. We have serviced homes and commercial sites across the region for many years, and we take pride in safe, tidy and reliable installations. This letter confirms the details of the work completed at your property and outlines the next steps for your records.</p>
      <p class="body-text">All wiring, switchboard upgrades and lighting fittings were tested on completion and meet current standards. A compliance certificate has been lodged and a copy is enclosed. Should you notice any fault or have questions about the new circuits, please call our office and a licensed electrician will attend promptly.</p>
      <p class="body-text">We also offer scheduled maintenance plans for homes and businesses. Ask us about a free site inspection and quote at a time that suits you.</p>
      <div class="signature">
        <div class="signature-name">Martin Fallow</div>
        <div class="signature-role">Company Director</div>
      </div>
    </article>

    <footer class="footer-note">
      <span class="label">Lic. No</span> 48162 / <span class="label">ABN:</span> 42 597 214 630
    </footer>
  </main>
</body>
</html>
```